Data Analytics Irish company needs Stationery Design

We need a stationery design for our data analytics company based in Dublin called 'Numbryx': we develop innovative web-based corporate applications exploiting advanced Machine Learning and Data Mining techniques.
Like the animal that inspired our company name, the final design should communicate intelligence and passion; on the other hand, we want to keep the highest professional appeal.
We love our current logo and we have tried out several color variations: we prefer solutions (see the logo attached) with white design and dark backgrounds, but we will also be glad to see some designs that follow the colors of the palette of the attached web screenshot.

```html
<!DOCTYPE html>
<html lang="en">
<head>
<meta charset="utf-8">
<title>Numbryx — Business Card</title>
<link rel="stylesheet" href="https://fonts.googleapis.com/css2?family=Comfortaa:wght@400&family=Tinos:wght@700&display=swap">
<style>
  :root {
    --page: #ffffff;
    --card-front: #2a2a2a;
    --card-back: #343434;
    --card-back-deep: #2b2b2b;
    --ink: #ffffff;
  }
  * { margin: 0; padding: 0; box-sizing: border-box; }
  html, body {
    width: 1200px;
    height: 343px;
    overflow: hidden;
    background: var(--page);
  }
  .sheet {
    position: relative;
    width: 1200px;
    height: 343px;
  }
  .card {
    position: absolute;
    top: 0;
    height: 343px;
    color: var(--ink);
  }
  .card--front {
    left: 0;
    width: 557px;
    background: var(--card-front);
  }
  .card--back {
    left: 621px;
    width: 579px;
    background: radial-gradient(ellipse at 30% 60%, var(--card-back) 0%, var(--card-back-deep) 75%);
  }
  .brand {
    font-family: "Comfortaa", sans-serif;
    font-weight: 400;
    color: var(--ink);
    letter-spacing: 1px;
    line-height: 1;
  }
  .front-mark {
    position: absolute;
    left: 140px;
    top: 40px;
  }
  .card--front .brand {
    position: absolute;
    left: 66px;
    top: 248px;
    font-size: 50px;
  }
  .card--back .brand {
    position: absolute;
    right: 62px;
    top: 58px;
    font-size: 56px;
  }
  .contact {
    position: absolute;
    left: 318px;
    top: 154px;
    font-family: "Tinos", serif;
    font-weight: 700;
    font-size: 17px;
    line-height: 1.05;
    list-style: none;
  }
  .contact li { margin-bottom: 15px; }
  .contact .address { margin-bottom: 17px; }
</style>
</head>
<body>
  <main class="sheet">
    <section class="card card--front" aria-label="Business card front">
      <svg class="front-mark" width="160" height="160" viewBox="0 0 160 160" aria-hidden="true">
        <circle cx="80" cy="80" r="78" fill="var(--ink)"/>
      </svg>
      <p class="brand">numbryx</p>
    </section>

    <section class="card card--back" aria-label="Business card back">
      <p class="brand">numbryx</p>
      <ul class="contact">
        <li class="address">214 Larkfield Road,<br>Dublin, D6W 2K7</li>
        <li>t: 555.555.5555</li>
        <li>hello@numbryx.com</li>
        <li>www.numbryx.com</li>
      </ul>
    </section>
  </main>
</body>
</html>
```